TAMBRIX passionate and energetic Business Card

We need a business card design for a new company based in Melbourne called "TAMBRIX" www.tambrix.com.au. We delivery food to the customer, we got 80+ restaurant at the moment. We would like to see designs that use the color red pearl white. The final design should be looks passionate and energetic. Should be related to the website www.tambrix.com.au

Target Market(s)

18-55 AGE

Industry/Entity Type

Business

Contact Information for Business Card

Fast Easy way to get food order on the internet.

Font styles to use
Serif
Sans Serif
Decorative

Colors
ec1f27
fff5ef

Requirements
Must have
• Should relative to the website www.tambrix.com.au
Nice to have
• No Idea
Should not have
• No Idea

```html
<!DOCTYPE html>
<html lang="en">
<head>
<meta charset="utf-8">
<title>TAMBRIX Business Card</title>
<link rel="stylesheet" href="https://fonts.googleapis.com/css2?family=Lobster&family=Roboto+Condensed:wght@400;700&display=swap">
<style>
  :root {
    --canvas: #ffffff;
    --card-black: #070908;
    --card-base: #e4dbcf;
    --red-start: #f5321a;
    --red-end: #cf0a20;
    --red-text: #c8102e;
    --pearl: #fff5ef;
    --white: #ffffff;
  }
  html, body {
    margin: 0;
    padding: 0;
    width: 1200px;
    height: 1000px;
    overflow: hidden;
    background: var(--canvas);
  }
  .canvas {
    position: relative;
    width: 1200px;
    height: 1000px;
  }
  .card-front {
    position: absolute;
    left: 170px;
    top: 410px;
    width: 284px;
    height: 173px;
    background: var(--card-black);
    display: flex;
    align-items: center;
    justify-content: center;
  }
  .brand-name {
    font-family: "Lobster", cursive;
    font-size: 50px;
    color: var(--pearl);
    letter-spacing: 1px;
  }
  .card-back {
    position: absolute;
    left: 680px;
    top: 290px;
    width: 415px;
    height: 414px;
    background: var(--card-base);
    overflow: hidden;
  }
  .red-band {
    position: absolute;
    left: 105px;
    width: 205px;
    background: linear-gradient(135deg, var(--red-start), var(--red-end));
  }
  .band-top { top: 0; height: 14px; }
  .band-name { top: 28px; height: 92px; }
  .band-company { top: 311px; height: 103px; }
  .contact-script {
    position: absolute;
    left: 105px;
    width: 205px;
    text-align: center;
    font-family: "Lobster", cursive;
    white-space: nowrap;
  }
  .person-name { top: 78px; font-size: 33px; color: var(--white); }
  .person-role { top: 124px; font-size: 32px; color: var(--white); text-shadow: 0 0 2px var(--red-text); }
  .phone { top: 168px; font-size: 27px; color: var(--red-text); }
  .email { top: 207px; font-size: 21px; color: var(--red-text); }
  .company-block {
    position: absolute;
    left: 105px;
    top: 320px;
    width: 205px;
    text-align: center;
    font-family: "Roboto Condensed", sans-serif;
    color: var(--white);
  }
  .company-name { font-size: 18px; font-weight: 700; line-height: 22px; }
  .company-line { font-size: 15px; line-height: 20px; }
  .company-web { font-size: 18px; font-weight: 700; line-height: 26px; margin-top: 2px; }
</style>
</head>
<body>
<main class="canvas">
  <section class="card-front" aria-label="Card front">
    <span class="brand-name">Tambrix</span>
  </section>

  <section class="card-back" aria-label="Card back">
    <div class="red-band band-top"></div>
    <div class="red-band band-name"></div>
    <div class="red-band band-company"></div>

    <div class="contact-script person-name">Daniel Reeves</div>
    <div class="contact-script person-role">CEO</div>
    <div class="contact-script phone">+61 0742 318 56</div>
    <div class="contact-script email">info@tambrix.com.au</div>

    <div class="company-block">
      <div class="company-name">Tambrix group</div>
      <div class="company-line">48 Collins Lane</div>
      <div class="company-line">Melbourne</div>
      <div class="company-web">www.tambrix.com.au</div>
    </div>
  </section>
</main>
</body>
</html>
```